Dravonel Semi truck

Hello Designers! I represent a truck driving company in need of a design for our new company trucks & trailers (new Tarmex, Brantholm & roadmaster pellucine). I want it modern, not too complicated, & eye catching. I will attach the logo, you can incorporate the symbol as part of the design. If desired, "Haul dravonel" can be added to the trailer. The trucks & trailers are going to be white.
I want the back door of the trailer to have our logo or haul4dravonel.com
The attached picture of the truck is grey and the logo is gold. The trucks are going to be the same but in white, so we will use the blue Dravonel Logo. We are also not sure if we want anything on the cab because we don't want it to feel overwhelming. If you have any questions please ask at mirela@dravonel.com. We will tip well for the design we pick. Thank you!

Target Market(s)

Drivers on the road

Industry/Entity Type

Truck driving company

Colors
0094D4
00A9DD
6FCCEA
C7EBF8
E9F6FB

Requirements
Must have
• Our website address to be included on the trailer (not in large print, medium-small): www. hauldravonel .com
Nice to have
• Some kind of pattern on the trailer, possibly cab as well.
Should not have
• any other bright colors other then the logo. A simple line is fine but nothing competing with the logo.

```html
<!DOCTYPE html>
<html lang="en">
<head>
<meta charset="utf-8">
<title>Dravonel trailer wrap panels</title>
<link rel="stylesheet" href="https://fonts.googleapis.com/css2?family=Jost:wght@600&family=Oswald:wght@600&display=swap">
<style>
  :root {
    --backdrop: #e6e6e6;
    --panel: #ffffff;
    --panel-edge: #8a8a8a;
    --teal: #6bbbbf;
    --navy: #1f5568;
  }
  * { margin: 0; padding: 0; box-sizing: border-box; }
  html, body { width: 711px; height: 1200px; overflow: hidden; background: var(--backdrop); }
  .canvas { position: relative; width: 711px; height: 1200px; }

  .panel {
    position: absolute;
    background: var(--panel);
    border: 1px solid var(--panel-edge);
    overflow: hidden;
  }
  .panel svg.pattern { position: absolute; inset: 0; width: 100%; height: 100%; }
  .pattern polygon { fill: var(--teal); }

  .brand {
    position: absolute;
    display: flex;
    align-items: center;
    font-family: "Jost", "Futura", sans-serif;
    font-weight: 600;
    color: var(--navy);
    white-space: nowrap;
  }
  .brand .mark { display: block; border-radius: 50%; background: var(--navy); }

  .web {
    position: absolute;
    font-family: "Oswald", "Arial Narrow", sans-serif;
    font-weight: 600;
    color: var(--navy);
    white-space: nowrap;
  }

  /* main side panel */
  .side-long { left: 36px; top: 408px; width: 640px; height: 147px; }
  .side-long .brand { left: 212px; top: 40px; font-size: 36px; gap: 14px; }
  .side-long .brand .mark { width: 52px; height: 52px; }
  .side-long .web { left: 6px; bottom: 6px; font-size: 9.5px; }

  /* short side panel */
  .side-short { left: 36px; top: 605px; width: 440px; height: 101px; }
  .side-short .brand { left: 146px; top: 30px; font-size: 24px; gap: 10px; }
  .side-short .brand .mark { width: 34px; height: 34px; }
  .side-short .web { right: 6px; bottom: 5px; font-size: 6.5px; }

  /* rear door panel */
  .rear-door { left: 500px; top: 605px; width: 176px; height: 186px; }
  .rear-door .phone { position: absolute; left: 19px; top: 12px; font-family: "Oswald", "Arial Narrow", sans-serif; font-weight: 600; font-size: 16px; color: var(--navy); }
  .rear-door .web { left: 19px; top: 36px; font-size: 8.5px; }
  .rear-door .brand { left: 14px; top: 90px; font-size: 18px; gap: 6px; }
  .rear-door .brand .mark { width: 22px; height: 22px; }
</style>
</head>
<body>
<main class="canvas">

  <section class="panel side-long">
    <svg class="pattern" viewBox="0 0 1250 288" preserveAspectRatio="none" role="img" aria-label="Teal diagonal parallelogram tile pattern">
      <polygon points="85,0 255,0 405,288 235,288"/>
      <polygon points="840,0 1250,0 1250,288 985,288"/>
    </svg>
    <div class="brand"><span class="mark"></span>Dravonel</div>
    <p class="web">www.hauldravonel.com</p>
  </section>

  <section class="panel side-short">
    <svg class="pattern" viewBox="0 0 861 198" preserveAspectRatio="none" role="img" aria-label="Teal diagonal parallelogram tile pattern">
      <polygon points="0,0 280,0 175,198 0,198"/>
      <polygon points="720,0 800,0 700,198 580,198"/>
    </svg>
    <div class="brand"><span class="mark"></span>Dravonel</div>
    <p class="web">www.hauldravonel.com</p>
  </section>

  <section class="panel rear-door">
    <svg class="pattern" viewBox="0 0 270 285" preserveAspectRatio="none" role="img" aria-label="Teal diagonal stripe pattern">
      <polygon points="262,0 270,0 270,235 130,235"/>
      <polygon points="0,252 270,252 270,285 0,285"/>
    </svg>
    <p class="phone">315-555-0142</p>
    <p class="web">www.hauldravonel.com</p>
    <div class="brand"><span class="mark"></span>Dravonel</div>
  </section>

</main>
</body>
</html>
```